依頼詳細
いまあるサンプルを春らしく変えて頂いても結構ですし、違うイメージで一から作成して頂いても結構です。このサンプルデザインに特にこだわりがあるわけではありませんので、良いデザインがあればどんどんご提案下さい。

対象が女性の50代~70代になるのでデザインのおしゃれさも大事ですが、シンプルでわかりやすいデザインを希望します。

A3サイズとB4サイズで作成をして下さい。
内容はまったく同じで用紙に合わせてレイアウトを調整して下さい。

真ん中部分の広告商品の商品名や価格はダミーで入れて頂ければ後から私が加筆します。

今後は季節ごとに配色を変えたり、季節感のある物を軽く挿入する程度で、作って頂いたデザインを通年使用していく予定です。

2ヶ月ごとに新聞広告の作成がありますので、今後ともよろしくお願いします。

選択させて頂いた広告の著作権(財産権)等は当方に譲渡をお願いします。フォントや画像素材などを利用する場合は上記利用用途に使用できることを確認し、第三者の知的財産権等に注意して下さい。
記載項目
会期 4月5日(火)~10日(日)

営業時間 10:00~18:00(最終日のみ15:00迄)

会場 アサギリモール一階・北側 SPACEはなゆき 京都市北区雲井南梅枝町38-6

主催 株式会社明葉 京都市北区雲井西竹丘町17-42 tel075-555-0183

2015年4月のサンプルにあるネットショップとブログの案内は省いて下さい。
サイズ
A3
ページ数
片面
希望イメージ
シンプル 複雑
単色 カラフル
暗い 明るい
日常 高級
遊び心 厳粛
未来的 伝統的
女性的 男性的
希望する色
納品ファイル
• 高解像度JPG (.jpg)
• イラストレーター形式 (.ai)
• フォトショップ形式 (.psd)
補足説明
サンプルを添付をさせて頂きます
たくさんのすばらしいデザインを作成して頂き、皆様本当にありがとうございます。

良いデザインばかりなので選定作業が困難を極めています(笑)

採用させて頂いた方はもちろん、それ以外の方も今後ともよろしくお願い申し上げます。

ありがとうございました。
■ 選んだ理由

女性のデザイナーさんらしくやさしさが伝わってきました。

■ 提案者全員のお礼・コメント

皆様本当にありがとうございました。明葉の広告をこんなたくさんの方にデザインしていただきうれしく思います。今後もよろしくお願いします。

```html
<!DOCTYPE html>
<html lang="ja">
<head>
<meta charset="utf-8">
<title>明葉の婦人服 春祭り</title>
<link rel="stylesheet" href="https://fonts.googleapis.com/css2?family=Noto+Serif+JP:wght@700;900&family=M+PLUS+Rounded+1c:wght@500;700;800&display=swap">
<style>
  :root{
    --plum:#5b2762;
    --plum-soft:#7a3f7f;
    --pink:#e0609a;
    --pink-deep:#d83d83;
    --pink-light:#f6c9dc;
    --blush:#fbe3ee;
    --white:#ffffff;
    --ink:#3a2a3a;
  }
  *{margin:0;padding:0;box-sizing:border-box;}
  html,body{overflow:hidden;}
  body{width:846px;height:1200px;}
  .poster{
    position:relative;width:846px;height:1200px;overflow:hidden;
    font-family:"M PLUS Rounded 1c",sans-serif;color:var(--plum);
    background:var(--blush);
  }
  .blossom-bg{
    position:absolute;inset:0;
    background:
      radial-gradient(circle at 85% 12%, #f2a9c8 0, rgba(242,169,200,0) 38%),
      radial-gradient(circle at 10% 55%, #f7c4da 0, rgba(247,196,218,0) 35%),
      radial-gradient(circle at 90% 70%, #f4b3cf 0, rgba(244,179,207,0) 35%),
      linear-gradient(180deg,#f8d3e3 0%,#fce9f1 45%,#f6c7db 100%);
  }
  .title{font-family:"Noto Serif JP",serif;font-weight:900;color:var(--plum);line-height:1;}
  .title-brand{position:absolute;left:118px;top:30px;font-size:140px;letter-spacing:10px;white-space:nowrap;}
  .title-main{position:absolute;left:118px;top:188px;font-size:122px;letter-spacing:2px;white-space:nowrap;}
  .title-no{
    position:absolute;left:392px;top:142px;width:72px;height:72px;border-radius:50%;
    background:var(--pink);color:var(--white);font-size:44px;display:flex;align-items:center;justify-content:center;
  }
  .festival-mark{position:absolute;left:500px;top:40px;width:236px;height:236px;border-radius:50%;
    background:radial-gradient(circle at 40% 35%,#f07fb0,#d94a8a);}
  .headline{position:absolute;left:0;right:0;top:320px;text-align:center;font-size:44px;line-height:52px;font-weight:800;color:var(--plum);letter-spacing:2px;}
  .lead{position:absolute;left:0;right:0;top:380px;text-align:center;font-size:16px;line-height:22px;font-weight:500;color:var(--plum-soft);}
  .section-band{
    position:absolute;left:40px;right:40px;top:418px;height:44px;
    background:linear-gradient(90deg,rgba(224,96,154,0),var(--pink) 18%,var(--pink) 82%,rgba(224,96,154,0));
    color:var(--white);font-size:25px;font-weight:700;text-align:center;line-height:44px;letter-spacing:3px;
  }
  .items{position:absolute;left:40px;top:484px;width:766px;display:grid;grid-template-columns:repeat(3,1fr);gap:14px 14px;}
  .item{background:var(--white);height:100px;border-radius:4px;box-shadow:0 2px 6px rgba(150,60,110,.15);
    display:flex;flex-direction:column;justify-content:space-between;padding:10px 14px;position:relative;}
  .item::before{content:"";position:absolute;left:0;top:0;width:0;height:0;border-top:18px solid var(--pink);border-right:18px solid transparent;}
  .item-name{font-size:15px;font-weight:700;color:var(--plum);line-height:1.3;padding-left:8px;}
  .item-price{font-size:32px;line-height:40px;font-weight:800;color:var(--pink-deep);text-align:right;border-top:1px solid var(--pink-light);padding-top:2px;}
  .item-price small{font-size:20px;}
  .label-circle{position:absolute;left:34px;width:70px;height:70px;border-radius:50%;background:var(--pink);color:var(--white);
    font-size:22px;font-weight:700;display:flex;align-items:center;justify-content:center;}
  .label-date{top:880px;}
  .label-venue{top:1000px;}
  .dates{position:absolute;left:120px;top:866px;font-size:62px;line-height:80px;font-weight:800;color:var(--plum);letter-spacing:1px;white-space:nowrap;}
  .dates small{font-size:32px;}
  .hours{position:absolute;left:126px;top:952px;font-size:18px;line-height:24px;font-weight:500;color:var(--plum);}
  .venue-name{position:absolute;left:120px;top:1004px;font-size:44px;line-height:60px;font-weight:800;color:var(--plum);white-space:nowrap;}
  .venue-mall{position:absolute;left:440px;top:998px;font-size:15px;line-height:22px;font-weight:700;color:var(--plum);white-space:nowrap;}
  .venue-access{position:absolute;left:440px;top:1026px;background:var(--ink);color:var(--white);font-size:11px;line-height:16px;padding:2px 6px;white-space:nowrap;}
  .venue-address{position:absolute;left:440px;top:1050px;font-size:12px;line-height:18px;font-weight:500;color:var(--plum);white-space:nowrap;}
  .map{position:absolute;left:652px;top:994px;width:164px;height:72px;background:#f3f0ee;border:1px solid #d9c4cf;}
  .site-url{position:absolute;right:30px;top:1072px;font-size:24px;line-height:30px;font-weight:800;color:var(--pink-deep);}
  .footer{position:absolute;left:0;right:0;top:1110px;height:90px;background:var(--white);}
  .footer-brand{position:absolute;left:30px;top:1136px;display:flex;align-items:center;gap:10px;font-size:28px;line-height:36px;font-weight:800;color:var(--pink-deep);letter-spacing:2px;}
  .footer-brand .dot{width:14px;height:14px;border-radius:50%;background:var(--pink);}
  .organizer{position:absolute;left:290px;top:1144px;font-size:14px;line-height:24px;font-weight:500;color:var(--ink);white-space:nowrap;}
  .organizer b{font-size:19px;font-weight:800;color:var(--plum);margin:0 12px 0 2px;}
</style>
</head>
<body>
<div class="poster">
  <div class="blossom-bg" role="img" aria-label="Soft pink cherry blossom background"></div>

  <h1 class="title">
    <span class="title-brand">明葉</span>
    <span class="title-main">婦人服</span>
    <span class="title-no">の</span>
  </h1>
  <div class="festival-mark" role="img" aria-label="Brush lettering 春祭り in white on a pink circle"></div>

  <p class="headline">今回もお値打ち品多数!!</p>
  <p class="lead">品質・価格に自信をもって取り揃えております。ご来店下さい。</p>

  <div class="section-band">春物・夏物・特別価格</div>

  <div class="items">
    <div class="item"><div class="item-name">チュニック各種（S～LL）</div><div class="item-price">2,900<small>円～</small></div></div>
    <div class="item"><div class="item-name">カーディガン各種（日本製）</div><div class="item-price">4,900<small>円～</small></div></div>
    <div class="item"><div class="item-name">シルクスカーフ<br>ネックカバー各種</div><div class="item-price">1,000<small>円～</small></div></div>
    <div class="item"><div class="item-name">綿・テンセルTシャツ各種<br>（日本製）</div><div class="item-price">2,900<small>円～</small></div></div>
    <div class="item"><div class="item-name">パンツ各種（7号～15号）</div><div class="item-price">3,900<small>円～</small></div></div>
    <div class="item"><div class="item-name">ジャケット各種（S～LL）</div><div class="item-price">5,900<small>円～</small></div></div>
  </div>

  <div class="label-circle label-date">会期</div>
  <div class="dates">4月5日<small>(火)</small>～10日<small>(日)</small></div>
  <div class="hours">10:00 ～ 18:00（最終日のみ 15:00 迄）</div>

  <div class="label-circle label-venue">場所</div>
  <div class="venue-name">SPACEはなゆき</div>
  <div class="venue-mall">アサギリモール 1階・北側</div>
  <div class="venue-access">地下鉄：朝霧駅 1番出口すぐ</div>
  <div class="venue-address">京都市北区雲井南梅枝町38-6</div>
  <div class="map" role="img" aria-label="Access map to the venue"></div>

  <div class="site-url">http://hanaakari.jp/</div>

  <div class="footer"></div>
  <div class="footer-brand"><span class="dot"></span>HANAAKARI</div>
  <div class="organizer">主催：<b>株式会社明葉</b>京都市北区雲井西竹丘町17-42　tel075-555-0183</div>
</div>
</body>
</html>
```